New Business Card Design Project

Need a design that will create an impact / strong impression towards our clients for our business. We are in the lighting business and we do lighting retrofits for large commercial to industrial clientele.

Target Market(s)

Lighting Industry

Industry/Entity Type

Business

Font styles to use
Other font styles liked:
• we would like to use the font on our logo, not sure what it is though..

Requirements
Must have
• Our logo.
Nice to have
• We are open to suggestions that have to do with lighting.

```html
<!DOCTYPE html>
<html lang="en">
<head>
<meta charset="utf-8">
<title>Brightline Retrofit Co. — Business Card</title>
<link href="https://fonts.googleapis.com/css2?family=Lato:wght@400;700;900&display=swap" rel="stylesheet">
<style>
  :root {
    --backdrop: #3a3a3c;
    --forest: #133f12;
    --green: #138a3a;
    --green-dark: #0e4a16;
    --ink: #1b1b1b;
    --paper: #ffffff;
    --soft: #d8e9d3;
  }
  * { box-sizing: border-box; margin: 0; padding: 0; }
  html, body { width: 1200px; height: 900px; overflow: hidden; }
  body {
    background: var(--backdrop);
    font-family: "Lato", sans-serif;
    position: relative;
  }
  .card {
    position: absolute;
    left: 240px;
    width: 720px;
    height: 411px;
    overflow: hidden;
  }
  .card-front { top: 24px; background: var(--forest); color: var(--paper); }
  .card-back { top: 462px; background: var(--paper); color: var(--ink); }

  .front-brand {
    position: absolute; left: 0; right: 0; top: 130px;
    text-align: center;
  }
  .brand-name {
    display: inline-flex; align-items: center; gap: 14px;
    font-weight: 900; font-size: 44px; letter-spacing: 1px;
  }
  .brand-square { width: 30px; height: 30px; background: currentColor; }
  .front-brand .brand-name { color: var(--soft); }
  .front-web {
    position: absolute; left: 0; right: 0; top: 320px;
    text-align: center; font-size: 20px; letter-spacing: 2px; color: var(--paper);
  }

  .back-brand { position: absolute; left: 40px; top: 34px; }
  .back-brand .brand-name { color: var(--green); font-size: 36px; gap: 12px; }
  .back-brand .brand-square { width: 24px; height: 24px; }

  .person { position: absolute; left: 40px; top: 118px; }
  .person-name { font-weight: 700; font-size: 31px; color: var(--green); }
  .person-role { font-size: 21px; margin-top: 2px; }

  .contacts { position: absolute; left: 40px; top: 208px; list-style: none; }
  .contacts li {
    display: flex; align-items: center; gap: 12px;
    font-size: 21px; line-height: 30px;
  }
  .contacts svg { width: 18px; height: 18px; fill: var(--green); flex: none; }

  .address {
    position: absolute; right: 44px; top: 262px;
    text-align: right; font-size: 22px; line-height: 30px;
  }

  .footer-band { position: absolute; left: 0; top: 340px; width: 720px; height: 36px; }
  .footer-web {
    position: absolute; left: 40px; top: 343px;
    font-size: 22px; color: var(--paper); letter-spacing: 0.5px;
  }
</style>
</head>
<body>

  <section class="card card-front">
    <div class="front-brand">
      <span class="brand-name"><span class="brand-square"></span>Brightline Retrofit Co.</span>
    </div>
    <p class="front-web">www.brightline-retrofit.com</p>
  </section>

  <section class="card card-back">
    <div class="back-brand">
      <span class="brand-name"><span class="brand-square"></span>Brightline Retrofit Co.</span>
    </div>

    <div class="person">
      <p class="person-name">Evan Marlow</p>
      <p class="person-role">Manager</p>
    </div>

    <ul class="contacts">
      <li>
        <svg viewBox="0 0 24 24" aria-hidden="true"><path d="M6.6 10.8a15.1 15.1 0 0 0 6.6 6.6l2.2-2.2a1 1 0 0 1 1-.25 11.4 11.4 0 0 0 3.6.57 1 1 0 0 1 1 1V20a1 1 0 0 1-1 1A17 17 0 0 1 3 4a1 1 0 0 1 1-1h3.5a1 1 0 0 1 1 1c0 1.25.2 2.45.57 3.57a1 1 0 0 1-.25 1z"/></svg>
        (555) 014-2270
      </li>
      <li>
        <svg viewBox="0 0 24 24" aria-hidden="true"><path d="M6 2h12v5H6z M4 8h16a2 2 0 0 1 2 2v7h-4v5H6v-5H2v-7a2 2 0 0 1 2-2z M8 15v5h8v-5z"/></svg>
        (555) 014-2271
      </li>
      <li>
        <svg viewBox="0 0 24 24" aria-hidden="true"><path d="M2 5h20v14H2z M3.5 6.5 12 13l8.5-6.5v-0.01z" fill-rule="evenodd"/></svg>
        hello@brightline-retrofit.com
      </li>
    </ul>

    <p class="address">1840 Larkspur Avenue<br>Fairmont, IL 60400</p>

    <svg class="footer-band" viewBox="0 0 720 36" aria-hidden="true">
      <polygon points="0,0 600,0 588,36 0,36" fill="var(--green)"/>
      <polygon points="608,0 660,0 648,36 596,36" fill="var(--green-dark)"/>
      <polygon points="672,0 720,0 720,36 660,36" fill="var(--green)"/>
    </svg>
    <p class="footer-web">www.brightline-retrofit.com</p>
  </section>

</body>
</html>
```